We are a organisation that provide outdoor adventure based tours to international students in New Ze

We are a Waikato New Zealand based company that runs adventure and outdoor tours around New Zealand. Activities included in our tours are mountain biking, rafting, sea kayaking, surfing/SUPing, luge, high ropes course, tramping, snorkelling and cultural activities. We need a Name/Logo, advertisement and information Flyers that we can give to the students/customers ASAP. We still haven't come up with a name so are hoping that designers can be more creative than we are. we are running our fist trip Dec 15th-22nd 2013.

Attached are some bits of information that we need to be included in the flyer. We need to get the 'Brightwater Tour' filled up first and the 'Kestrel's Cove Tour' will be later.

We want it to be an exciting and edgy design with an 'outdoor' feel to it. There is the potential for this design to be expanded into our website.

The brochure/ Flyer can come in any creative format.

Target Market(s)

High school aged students. We will be expanding to University students in the future. We also need to make sure that this is appealing to the parents. It will be them who will agree to them going on the trips after all.

Industry/Entity Type

It Company

Requirements
Must have
• Our Contact details.
Booking Info
Tour information from attached.
Nice to have
• Photos can use the ones we have put into the attachment or other images from the outdoors that designers can source to make it look good.

```html
<!DOCTYPE html>
<html lang="en">
<head>
<meta charset="utf-8">
<title>Kestrel's Cove Tour Flyer</title>
<link href="https://fonts.googleapis.com/css2?family=Bebas+Neue&family=Big+Shoulders+Display:wght@200&display=swap" rel="stylesheet">
<style>
:root{
  --paper:#ffffff;
  --slate:#3a3a3a;
  --slate-deep:#2c2c2c;
  --cyan:#27e6f0;
  --red:#e8453a;
  --green:#45d94a;
  --orange:#f5a623;
  --chalk:#ffffff;
  --text:#f2f2f2;
}
*{margin:0;padding:0;box-sizing:border-box}
html,body{width:1096px;height:1200px;overflow:hidden;background:var(--paper)}
.flyer{position:relative;width:1096px;height:1200px;background:var(--paper);font-family:'Bebas Neue',sans-serif;color:var(--text)}
.panel{position:absolute;left:256px;top:0;width:840px;height:1082px;background:var(--slate)}
.abs{position:absolute}
.photo{position:absolute;border:7px solid var(--chalk);box-shadow:0 0 0 1px #ddd}
.photo-raft{left:832px;top:7px;width:198px;height:192px;background:linear-gradient(160deg,#4e7a3a,#2f5a2a 45%,#cfd8d4 60%,#e7c63a 75%,#4a6a3a)}
.photo-snorkel{left:352px;top:932px;width:206px;height:139px;background:linear-gradient(180deg,#9cc8e8 0%,#cfe3f0 35%,#2f8fbf 55%,#1c6b9a 100%)}
.title-band{left:272px;top:128px;width:404px;height:124px}
.tour-title{left:282px;top:150px;font-family:'Big Shoulders Display',sans-serif;font-weight:200;font-size:64px;letter-spacing:2px;color:var(--chalk);line-height:1}
.spaces-box{left:667px;top:107px;width:210px;height:146px;background:var(--slate-deep)}
.limited{left:672px;top:120px;font-size:36px;line-height:48px;color:var(--red);-webkit-text-stroke:1px #ffd0c8;letter-spacing:1px}
.dates{left:696px;top:226px;font-size:24px;color:var(--chalk)}
.divider{left:650px;top:250px;width:50px;height:570px}
.intro{left:282px;top:280px;width:388px;font-size:18px;line-height:26.7px;letter-spacing:1.1px}
.list{left:286px;top:453px;list-style:none;font-size:17px;line-height:26.2px;letter-spacing:.5px}
.list li{display:flex}
.list .n{width:48px}
.costs-head{left:286px;top:822px;font-size:17px;color:var(--green)}
.costs{top:849px}
.offer{left:702px;top:268px;width:372px;font-size:27px;line-height:22px;color:var(--green);letter-spacing:.5px}
.days{left:704px;top:342px;width:390px;font-size:20px;line-height:26.4px;letter-spacing:.9px}
.booking{left:576px;top:833px;width:428px;height:215px;border:3px solid var(--chalk);border-radius:16px}
.booking-head{left:598px;top:838px;font-size:26px;color:var(--cyan);letter-spacing:1px}
.contact{font-size:20px;line-height:24px}
.contact .phone{position:absolute;left:248px;bottom:0}
.contact-a{left:592px;top:880px;color:var(--orange)}
.contact-b{left:592px;top:943px;color:var(--green)}
</style>
</head>
<body>
<div class="flyer">
  <div class="panel"></div>

  <svg class="abs title-band" viewBox="0 0 404 124" aria-hidden="true">
    <polygon fill="#27e6f0" points="6,10 120,4 260,8 398,2 402,30 396,62 402,96 392,120 250,116 120,122 8,114 2,80 10,50 0,26"/>
  </svg>
  <div class="abs tour-title">Kestrel's Cove Tour</div>

  <div class="abs spaces-box"></div>
  <div class="abs limited">Limited to<br>30 spaces</div>
  <div class="abs dates">January 24th-31st</div>

  <div class="photo photo-raft" role="img" aria-label="Photo of a raft crew going down a waterfall"></div>

  <svg class="abs divider" viewBox="0 0 50 570" aria-hidden="true">
    <polygon fill="#ffffff" points="18,0 34,4 30,110 36,240 28,370 34,480 30,570 16,566 20,460 14,350 22,220 16,100"/>
  </svg>

  <div class="abs intro">&nbsp;&nbsp;Kestrel's Cove Tour takes you on a journey to the golden beaches, crystal clear waters and lush native NZ bush of the Coromandel. We then make our way to New Zealands best adventure destinations Rotorua. Through to Taupo and the Central Plateau.<br>Activities we have included in the tour are:</div>

  <ul class="abs list">
    <li><span class="n">5.</span>Rafting</li>
    <li><span class="n">6.</span>Mountain Biking</li>
    <li><span class="n">7.</span>Luge/Thrill Rides</li>
    <li><span class="n">8.</span>Sea Kayaking Cathedral Cove</li>
    <li><span class="n">9.</span>Tramping</li>
    <li><span class="n">10.</span>Glass Bottom Boat</li>
    <li><span class="n">11.</span>Bungy</li>
    <li><span class="n">12.</span>Snorkeling</li>
    <li><span class="n">13.</span>Fishing</li>
    <li><span class="n">14.</span>High Ropes Course</li>
    <li><span class="n">15.</span>Hot Pools</li>
    <li><span class="n">16.</span>Sight Seeing</li>
    <li><span class="n">17.</span>Cultural Experience</li>
  </ul>

  <div class="abs costs-head">[ ncluded in the costs ]</div>
  <ul class="abs list costs">
    <li><span class="n">12.</span>Food</li>
    <li><span class="n">13.</span>All Transport</li>
    <li><span class="n">14.</span>Cost of all activities and guides</li>
  </ul>

  <div class="photo photo-snorkel" role="img" aria-label="Photo of a snorkeler in the sea beside a boat"></div>

  <div class="abs offer">&nbsp;All of this and 7days of fun with other international students for $1455pp</div>

  <div class="abs days">
    <p>Day 1 - Waikato high ropes course and travel to Papa Aroha Coromandel for some kiwi camping</p>
    <p>Day 2 - Travel to Whitianga and go on the 'glass bottom boat' and snorkeling in the marine reserve</p>
    <p>Day 3 - Kayak tours to Cathedral Cove and dig a spa at Hotwater Beach with fish and chips on the beach</p>
    <p>Day 4 - Travel to the Rotorua luge and skyrides. Later hit the geothermal hot pools and 'cultural night'</p>
    <p>Day 5 - Raft the Kaituna River and mountain biking Redwood Forests and BBQ night</p>
    <p>Day 6 - Travel to Taupo where you have the option to bungy jump and then we go to the mysterious 'Craters of the Moon'</p>
    <p>Day 7 - Huka Falls, natural hot springs and miniputt</p>
    <p>Day 8 - Travel and farewells</p>
  </div>

  <div class="abs booking"></div>
  <div class="abs booking-head">To make a booking contact either</div>
  <div class="abs contact contact-a">Tane Walker<br>tanewalker@kestrelmail.com<span class="phone">0225550143</span></div>
  <div class="abs contact contact-b">Rowan Pike<br>rowanpike@kestrelmail.com<span class="phone">0215550178</span></div>
</div>
</body>
</html>
```